Vexora Promo Consulting Company Website

Need a website for a consulting company that will help nonprofits qualify to get free online ads from Vexora in their Vexora Promo Bursary program and that will also help them manage the ad spend. Need a new logo as part of this. You can look at our current site at www.lumenhallow.com to get a sense as to content. I am looking for a nice looking site that will be easy to maintain and expand upon. It should load fast and be good design from an SEO perspective.
Updates

Need extra days to review

Target Market(s)

Midsized nonprofits.

Industry/Entity Type

nonprofit marketing

Coding

Coded - Design and coding required

Number of Pages Required

5+ page

```html
<!DOCTYPE html>
<html lang="en">
<head>
<meta charset="utf-8">
<title>Lumen Hallow — Vexora Promo Bursary Management</title>
<link href="https://fonts.googleapis.com/css2?family=Oswald:wght@500;700&family=Roboto:wght@400;500;700&display=swap" rel="stylesheet">
<style>
:root{
  --blue:#3b5ba9;
  --blue-dark:#2f4d96;
  --orange:#f47c22;
  --ink:#1d1d1f;
  --text:#555a63;
  --footer:#2b2b2d;
  --footer-text:#e6e6e6;
  --white:#ffffff;
  --accent-tint:#e9ecf3;
}
*{box-sizing:border-box;margin:0;padding:0}
html,body{width:1200px;height:4163px;overflow:hidden}
body{font-family:"Roboto",Arial,sans-serif;color:var(--text);background:var(--white);position:relative}
.abs{position:absolute}
.display{font-family:"Oswald","Arial Narrow",sans-serif;font-weight:700;text-transform:uppercase;letter-spacing:0}
.btn{position:absolute;background:var(--orange);color:#fff;font-size:13px;font-weight:700;display:flex;align-items:center;justify-content:center;gap:10px;border-radius:3px;text-transform:uppercase}
.btn .dot{width:12px;height:12px;border-radius:50%;background:#fff;position:relative}
.btn .dot::after{content:"";position:absolute;left:4px;top:3px;border-left:5px solid var(--orange);border-top:3px solid transparent;border-bottom:3px solid transparent}
.rule{position:absolute;height:3px;width:40px;background:var(--blue)}

/* hero */
.hero{position:absolute;left:0;top:0;width:1200px;height:643px;overflow:hidden}
.hero-photo{position:absolute;inset:0;background:linear-gradient(90deg,#fbeeea 0%,#f6e2da 35%,#d9b79a 55%,#a5876e 75%,#6f5a4d 100%)}
.logo{font-family:"Oswald",sans-serif;font-weight:700;font-size:32px;color:var(--blue);text-transform:uppercase}
.nav{position:absolute;top:32px;left:384px;display:flex;gap:21px;font-size:13px;font-weight:500;color:#fff}
.hero h1{position:absolute;left:110px;top:228px;font-size:43px;line-height:60px;color:var(--blue)}
.hero p{position:absolute;left:111px;top:355px;width:560px;font-size:18px;line-height:26px;color:#444}
.slider-dots{position:absolute;left:111px;top:530px;display:flex;gap:4px}
.slider-dots span{width:7px;height:7px;border-radius:50%;background:#1b2a4e}
.slider-dots span:first-child{background:var(--orange)}
.social-rail{position:absolute;left:1124px;top:212px;width:34px;display:flex;flex-direction:column;align-items:center;gap:12px}
.ring{border:2px solid #fff;border-radius:50%}
.scroll-text{position:absolute;left:1090px;top:420px;width:100px;text-align:center;transform:rotate(-90deg);color:#fff;font-size:12px;font-weight:700;white-space:nowrap}

/* about */
.kicker{font-family:"Oswald",sans-serif;font-weight:700;font-size:17px;color:var(--orange);text-transform:uppercase}
.photo{position:absolute}
.about-text{position:absolute;left:620px;top:860px;width:475px;font-size:13.5px;line-height:25px;color:var(--text)}

/* process */
.process{position:absolute;left:0;top:1192px;width:1200px;height:515px;background:var(--blue)}
.step{position:absolute;width:248px;height:248px;border-radius:50%;background:#fff;text-align:center;top:197px}
.step svg{position:absolute;left:100px;top:45px}
.step h3{position:absolute;top:104px;left:0;width:100%;font-size:13.5px;font-weight:700;color:var(--ink);text-transform:uppercase}
.step p{position:absolute;top:144px;left:34px;width:180px;font-size:12px;line-height:19px;color:#777}

/* worked with */
.worked p.body{position:absolute;left:111px;top:1985px;width:438px;font-size:13.5px;line-height:25px;text-align:justify}
.accent-block{position:absolute;background:var(--accent-tint)}

/* organize */
.organize{position:absolute;left:0;top:2374px;width:1200px;height:776px;background:linear-gradient(180deg,#f58a37,#f37a1f 60%,#f07a1e)}
.card{position:absolute;width:305px;height:191px;background:rgba(120,70,40,.18);border:1px solid rgba(255,255,255,.25)}
.card .ico{position:absolute;left:32px;top:-38px;width:76px;height:76px;background:var(--blue);display:flex;align-items:center;justify-content:center}
.card h4{position:absolute;left:25px;top:68px;font-family:"Oswald",sans-serif;font-size:13px;font-weight:700;color:#fff;text-transform:uppercase}
.card p{position:absolute;left:25px;top:94px;width:265px;font-size:13px;line-height:24px;color:#fff}

/* contact */
.form-label{position:absolute;font-size:13px;font-weight:700;color:var(--ink);text-transform:uppercase}
.form-value{position:absolute;font-size:11px;color:#777}
.form-line{position:absolute;height:1px;background:#ddd}

/* footer */
.footer{position:absolute;left:0;top:3779px;width:1200px;height:384px;background:var(--footer);color:var(--footer-text)}
.footer h5{position:absolute;font-size:18px;font-weight:700;color:#fff}
.footer .frule{position:absolute;width:30px;height:2px;background:var(--blue)}
.footer ul{position:absolute;list-style:none;font-size:13.5px;line-height:31px}
.footer li::before{content:"»";margin-right:12px}
.sq{position:absolute;width:34px;height:34px;border:1px solid #ddd}
</style>
</head>
<body>

<header class="hero">
  <div class="hero-photo" role="img" aria-label="Photo of a consultant in a tan blazer meeting a client in a bright office"></div>
  <div class="abs logo" style="left:103px;top:18px">Lumen Hallow</div>
  <nav class="nav"><span>HOME</span><span>ABOUT US</span><span>OUR SERVICES</span><span>PROCESS</span><span>INFORMATION CENTER</span></nav>
  <div class="btn" style="left:896px;top:19px;width:134px;height:42px">Contact Us <span class="dot"></span></div>
  <div class="abs" style="left:1053px;top:20px;width:42px;height:42px;border-radius:50%;background:var(--blue)">
    <svg width="42" height="42" viewBox="0 0 42 42"><circle cx="19" cy="19" r="6" fill="none" stroke="#fff" stroke-width="2.5"/><line x1="23.5" y1="23.5" x2="28" y2="28" stroke="#fff" stroke-width="2.5"/></svg>
  </div>
  <h1 class="display">Vexora Grant Management<br>From Expets You Can Trust</h1>
  <p>The Vexora Promo Bursary program is a must for all eligible charitable organizations.</p>
  <div class="btn" style="left:111px;top:430px;width:136px;height:43px">Get Started <span class="dot"></span></div>
  <div class="slider-dots"><span></span><span></span><span></span><span></span><span></span></div>
  <div class="social-rail" aria-label="Social links">
    <div class="ring" style="width:32px;height:32px"></div>
    <div class="ring" style="width:14px;height:14px;margin-top:8px"></div>
    <div style="width:14px;height:14px;border:2px solid #fff;border-radius:4px"></div>
    <div style="width:2px;height:55px;background:#fff;margin-top:14px"></div>
  </div>
  <div class="scroll-text">SCROLL DOWN</div>
  <svg class="abs" style="left:1131px;top:486px" width="20" height="36" viewBox="0 0 20 36"><circle cx="10" cy="9" r="8" fill="#ddd"/><line x1="10" y1="10" x2="10" y2="32" stroke="#fff" stroke-width="2"/><path d="M5 27 L10 33 L15 27" fill="none" stroke="#fff" stroke-width="2"/></svg>
</header>

<section class="about">
  <div class="photo" style="left:129px;top:740px;width:341px;height:298px;background:linear-gradient(135deg,#c9c4bd,#8d8a86 60%,#5d5c5a)" role="img" aria-label="Photo of a team meeting around an office table"></div>
  <div class="photo" style="left:338px;top:935px;width:190px;height:154px;background:linear-gradient(135deg,#b4b1ac,#6c6864 55%,#3f3c3a)" role="img" aria-label="Photo of colleagues reviewing documents together"></div>
  <div class="abs kicker" style="left:620px;top:742px">About Us</div>
  <h2 class="abs display" style="left:620px;top:776px;font-size:33px;color:var(--ink)">Vexora Ad Grants Acquisition</h2>
  <div class="rule" style="left:620px;top:831px"></div>
  <p class="about-text">The Vexora Promo Bursary program is a must for all eligible charitable organizations. It is a unique opportunity for organizations to extend their public service messages to a wider audience in an effort to gain new donors, attract volunteers, and further your organization's impact. The Vexora Promo Bursary program is a must for all eligible organizations. It is a unique opportunity for organizations to extend their public service messages to a wider audience</p>
  <div class="btn" style="left:620px;top:1047px;width:134px;height:45px">Learn More <span class="dot"></span></div>
</section>

<section class="process">
  <div class="abs display" style="left:0;width:1200px;top:75px;text-align:center;font-size:16px;color:#fff">Why Choose Us</div>
  <h2 class="abs display" style="left:0;width:1200px;top:102px;text-align:center;font-size:35px;color:#fff">Our Process</h2>
  <div class="abs" style="left:580px;top:163px;width:40px;height:3px;background:#fff"></div>

  <div class="step" style="left:110px">
    <svg width="48" height="48" viewBox="0 0 48 48" fill="none" stroke="#f47c22" stroke-width="2.5"><circle cx="12" cy="9" r="5"/><circle cx="24" cy="9" r="5"/><circle cx="36" cy="9" r="5"/><path d="M4 30v-8a6 6 0 0 1 12 0M18 30v-8a6 6 0 0 1 12 0M32 30v-8a6 6 0 0 1 12 0"/><line x1="4" y1="32" x2="44" y2="32"/><path d="M10 32v14M38 32v14M18 32v10M30 32v10"/></svg>
    <h3>Initial Consultation</h3>
    <p>Our Vexora Ad Grants are industry specialists. We work with every type of nonprofit</p>
  </div>
  <div class="step" style="left:354px">
    <svg width="48" height="48" viewBox="0 0 48 48" fill="none" stroke="#f47c22" stroke-width="2.5"><circle cx="24" cy="24" r="19" fill="#f47c22" fill-opacity=".15"/><ellipse cx="24" cy="24" rx="8" ry="19"/><line x1="5" y1="24" x2="43" y2="24"/><path d="M8 14h32M8 34h32"/></svg>
    <h3>Website Readiness</h3>
    <p>One of Vexora's eligibility requirements is to have a website the meets certain</p>
  </div>
  <div class="step" style="left:598px">
    <svg width="48" height="48" viewBox="0 0 48 48"><rect x="5" y="6" width="38" height="26" rx="2" fill="#f47c22"/><circle cx="24" cy="19" r="7" fill="#fff"/><path d="M20.5 19l2.5 2.5 4.5-4.5" fill="none" stroke="#f47c22" stroke-width="2"/><rect x="21" y="32" width="6" height="8" fill="#f47c22"/><rect x="14" y="40" width="20" height="3" fill="#f47c22"/></svg>
    <h3>Grant Acquisition</h3>
    <p>Sit back and leave your Vexora grants acquisition to us. If we need any documentation</p>
  </div>
  <div class="step" style="left:842px">
    <svg width="48" height="48" viewBox="0 0 48 48"><rect x="8" y="26" width="8" height="16" fill="#f47c22"/><rect x="20" y="16" width="8" height="26" fill="#f47c22"/><rect x="32" y="6" width="8" height="36" fill="#f47c22"/></svg>
    <h3>Vexora Promo Setup</h3>
    <p>If you do not have one already, our Vexora Promo specialists will help set up your Vexora</p>
  </div>
</section>

<section class="worked">
  <div class="abs kicker" style="left:111px;top:1838px;font-size:15px">We Have Worked With</div>
  <h2 class="abs display" style="left:111px;top:1868px;font-size:29px;line-height:36px;color:var(--ink)">Nonprofit Organizations<br>Large &amp; Small For Over 30 Years.</h2>
  <div class="rule" style="left:111px;top:1956px"></div>
  <p class="body">From formation, management, compliance, fundraising, etc. we have unmatched experience in the nonprofit sector. We are proud to have nonprofit fundraisers and current nonprofit volunteers in our team of nonprofit vexora grants management team.From formation, management, compliance, fundraising, etc. we have unmatched experience in the nonprofit sector. We are proud to have nonprofit fundraisers and current nonprofit volunteers in our team of nonprofit vexora grants management team.</p>
  <svg class="abs" style="left:110px;top:2203px" width="200" height="32" viewBox="0 0 200 32"><path d="M20 2 A14 14 0 1 0 20 30" fill="none" stroke="#3b5ba9" stroke-width="2"/><text x="26" y="20" font-family="Roboto" font-size="11.5" font-weight="700" fill="#3b5ba9">LEARN MORE ABOUT US</text><path d="M178 16h12M186 12l4 4-4 4" fill="none" stroke="#3b5ba9" stroke-width="1.6"/></svg>
  <div class="accent-block" style="left:612px;top:1806px;width:122px;height:66px" role="img" aria-label="Decorative accent block"></div>
  <div class="abs" style="left:640px;top:2067px;width:3px;height:202px;background:var(--orange)"></div>
  <div class="abs" style="left:640px;top:2266px;width:560px;height:3px;background:var(--orange)"></div>
  <div class="photo" style="left:662px;top:1833px;width:538px;height:412px;background:linear-gradient(120deg,#5b4a3d,#9a8170 45%,#c9b7a6 70%,#e2d6c8)" role="img" aria-label="Photo of two consultants discussing work at a laptop"></div>
</section>

<section class="organize">
  <div class="abs display" style="left:0;width:1200px;top:62px;text-align:center;font-size:15px;color:#fff">Your Account For You</div>
  <h2 class="abs display" style="left:0;width:1200px;top:90px;text-align:center;font-size:34px;color:#fff">What We Organize</h2>

  <div class="card" style="left:113px;top:225px"><div class="ico"><svg width="40" height="40" viewBox="0 0 40 40" fill="none" stroke="#fff" stroke-width="2.5"><rect x="7" y="4" width="22" height="30"/><path d="M12 12h12M12 18h12M12 24h8"/><path d="M34 14l-10 14-3 1 1-3 10-14z"/></svg></div><h4>Set Your Budget</h4><p>Lorem ipsum dolor sit amet, consectetur adipiscing elit, sed do eiusmod tempor incididunt ut labore et dolore</p></div>
  <div class="card" style="left:457px;top:225px"><div class="ico"><svg width="40" height="40" viewBox="0 0 40 40" fill="none" stroke="#fff" stroke-width="2.5"><circle cx="20" cy="10" r="5"/><circle cx="9" cy="16" r="4"/><circle cx="31" cy="16" r="4"/><path d="M12 30a8 8 0 0 1 16 0M3 30a6 6 0 0 1 9-5M37 30a6 6 0 0 0-9-5"/><path d="M8 35h24"/></svg></div><h4>Select Keywords</h4><p>Lorem ipsum dolor sit amet, consectetur adipiscing elit, sed do eiusmod tempor incididunt ut labore et dolore</p></div>
  <div class="card" style="left:799px;top:225px"><div class="ico"><svg width="40" height="40" viewBox="0 0 40 40" fill="none" stroke="#fff" stroke-width="2.5"><circle cx="20" cy="18" r="10"/><circle cx="20" cy="18" r="4"/><path d="M20 4v4M20 28v4M6 18h4M30 18h4M10 8l3 3M27 25l3 3M30 8l-3 3M10 28l3-3"/><path d="M15 36h10"/></svg></div><h4>Set Your Match Types</h4><p>Lorem ipsum dolor sit amet, consectetur adipiscing elit, sed do eiusmod tempor incididunt ut labore et dolore</p></div>

  <div class="card" style="left:113px;top:489px"><div class="ico"><svg width="40" height="40" viewBox="0 0 40 40" fill="#fff"><rect x="18" y="3" width="4" height="34"/><path d="M8 8h24l4 4-4 4H8z"/><path d="M32 19H10l-4 4 4 4h22z"/><rect x="12" y="35" width="16" height="3"/></svg></div><h4>Set Your Landing Page</h4><p>Lorem ipsum dolor sit amet, consectetur adipiscing elit, sed do eiusmod tempor incididunt ut labore et dolore</p></div>
  <div class="card" style="left:457px;top:489px"><div class="ico"><svg width="40" height="40" viewBox="0 0 40 40" fill="none" stroke="#fff" stroke-width="2.5"><rect x="4" y="5" width="32" height="24"/><path d="M9 12h22M9 18h14M9 23h18"/><path d="M16 29l-3 7M24 29l3 7M11 36h18"/></svg></div><h4>Mobile Phone</h4><p>Lorem ipsum dolor sit amet, consectetur adipiscing elit, sed do eiusmod tempor incididunt ut labore et dolore</p></div>
  <div class="card" style="left:799px;top:489px"><div class="ico"><svg width="40" height="40" viewBox="0 0 40 40" fill="none" stroke="#fff" stroke-width="2.5"><path d="M8 4v32"/><rect x="8" y="5" width="26" height="20"/><rect x="14" y="10" width="14" height="10"/><path d="M4 36h12"/></svg></div><h4>Connect Your Vexora Promo</h4><p>Lorem ipsum dolor sit amet, consectetur adipiscing elit, sed do eiusmod tempor incididunt ut labore et dolore</p></div>
</section>

<section class="contact">
  <div class="accent-block" style="left:121px;top:3524px;width:180px;height:110px" role="img" aria-label="Decorative accent block"></div>
  <div class="abs" style="left:147px;top:3259px;width:363px;height:307px;background:var(--blue)"></div>
  <div class="abs display" style="left:270px;top:3323px;font-size:15px;color:#fff">Contact Us</div>
  <div class="abs" style="left:392px;top:3325px;width:5px;height:16px;background:#fff"></div>
  <div class="abs display" style="left:150px;width:249px;top:3362px;text-align:right;font-size:47px;line-height:52px;color:#fff">Let's Go<br>Good<br>Together</div>
  <div class="abs" style="left:759px;top:3259px;width:292px;height:351px;border:4px solid var(--blue)"></div>
  <div class="abs" style="left:444px;top:3296px;width:570px;height:390px;background:#fff;box-shadow:0 4px 22px rgba(0,0,0,.08)"></div>
  <h2 class="abs display" style="left:484px;top:3326px;font-size:28px;color:var(--ink)">Send Us A Message</h2>
  <div class="form-label" style="left:484px;top:3390px">Your Name</div>
  <div class="form-value" style="left:484px;top:3424px">Jane Rivera</div>
  <div class="form-line" style="left:484px;top:3443px;width:232px"></div>
  <div class="form-label" style="left:738px;top:3390px">Company</div>
  <div class="form-value" style="left:738px;top:3424px">jane@lumenhallow.com</div>
  <div class="form-line" style="left:738px;top:3443px;width:232px"></div>
  <div class="form-label" style="left:484px;top:3471px">Email Address</div>
  <div class="form-value" style="left:484px;top:3505px">jane@lumenhallow.com</div>
  <div class="form-line" style="left:484px;top:3524px;width:232px"></div>
  <div class="form-label" style="left:738px;top:3471px">Phone</div>
  <div class="form-value" style="left:738px;top:3505px">1 555 010 0199</div>
  <div class="form-line" style="left:738px;top:3524px;width:232px"></div>
  <div class="form-label" style="left:484px;top:3558px">Message</div>
  <div class="form-value" style="left:484px;top:3590px">Hi , do you have a moment to talk about Us</div>
  <div class="form-line" style="left:484px;top:3635px;width:440px"></div>
  <svg class="abs" style="left:924px;top:3595px" width="52" height="52" viewBox="0 0 52 52"><circle cx="26" cy="26" r="26" fill="#f47c22"/><path d="M16 27l19-10-7 19-3-7z" fill="#fff"/></svg>
</section>

<footer class="footer">
  <div class="abs logo" style="left:111px;top:66px;font-size:32px">Lumen Hallow</div>
  <div class="sq" style="left:111px;top:147px" aria-label="Social link"></div>
  <div class="sq" style="left:161px;top:147px" aria-label="Social link"></div>
  <div class="sq" style="left:211px;top:147px" aria-label="Social link"></div>
  <div class="sq" style="left:260px;top:147px" aria-label="Social link"></div>

  <h5 style="left:397px;top:67px">Quick Links</h5>
  <div class="frule" style="left:397px;top:100px"></div>
  <ul style="left:397px;top:114px"><li>Home</li><li>About Us</li><li>Our Services</li><li>Latest Blog</li><li>Contact Us</li></ul>

  <h5 style="left:585px;top:67px">Our Services</h5>
  <ul style="left:585px;top:114px"><li>Initial Consultation</li><li>Website Readiness</li><li>Grant Acquisition</li><li>Vexora Promo Setup</li></ul>

  <h5 style="left:806px;top:67px">Contact Us</h5>
  <svg class="abs" style="left:806px;top:126px" width="12" height="16" viewBox="0 0 12 16"><path d="M6 0a6 6 0 0 1 6 6c0 4-6 10-6 10S0 10 0 6a6 6 0 0 1 6-6z" fill="#fff"/><circle cx="6" cy="6" r="2.2" fill="#2b2b2d"/></svg>
  <div class="abs" style="left:830px;top:122px;width:250px;font-size:13.5px;line-height:21px">Sed ut perspiciatis unde omnis iste natus error sit voluptatem</div>
  <svg class="abs" style="left:806px;top:180px" width="14" height="14" viewBox="0 0 14 14"><path d="M3 0l3 3-2 2a8 8 0 0 0 5 5l2-2 3 3-2 3C6 14 0 8 0 3z" fill="#fff"/></svg>
  <div class="abs" style="left:830px;top:177px;font-size:13.5px">Tel No :&nbsp; 1 555 010 0199</div>
  <svg class="abs" style="left:806px;top:218px" width="15" height="11" viewBox="0 0 15 11"><rect width="15" height="11" fill="#fff"/><path d="M0 0l7.5 6L15 0" fill="none" stroke="#2b2b2d" stroke-width="1.4"/></svg>
  <div class="abs" style="left:830px;top:213px;font-size:13.5px">Email&nbsp; :&nbsp; info@lumenhallow.com</div>

  <div class="abs" style="left:111px;top:297px;width:974px;height:1px;background:#666"></div>
  <div class="abs" style="left:111px;top:338px;font-size:13.5px">© 2021 Lumen Hallow. All Rights Reserved</div>
  <div class="abs" style="left:848px;top:338px;font-size:13.5px">Privacy Policy &nbsp; | &nbsp; Terms &amp; Conditions</div>
</footer>

</body>
</html>
```